Brimovex business card

Based on company logo and website given , to design a business card temple. Slogan "Your furry friends deserves the best"
Color style please refer to our website

```html
<!DOCTYPE html>
<html lang="en">
<head>
<meta charset="utf-8">
<title>Brimovex business card</title>
<link href="https://fonts.googleapis.com/css2?family=Montserrat:wght@400;500;700&display=swap" rel="stylesheet">
<style>
  :root {
    --stage: #2b2b2b;
    --card-top: #0d3f38;
    --card-bottom: #072a25;
    --gold: #c8c127;
    --ink-light: #d9dfdd;
  }
  * { box-sizing: border-box; margin: 0; padding: 0; }
  html, body { width: 1200px; height: 900px; overflow: hidden; }
  body {
    background: var(--stage);
    font-family: "Montserrat", Arial, sans-serif;
    display: flex;
    align-items: center;
    justify-content: center;
    gap: 40px;
  }
  .card {
    width: 540px;
    height: 309px;
    border-radius: 18px;
    background: linear-gradient(160deg, var(--card-top), var(--card-bottom));
    position: relative;
    color: var(--ink-light);
  }
  .wordmark {
    display: flex;
    align-items: center;
    gap: 10px;
    color: var(--gold);
    font-weight: 700;
    letter-spacing: 0.5px;
  }
  .wordmark-dot {
    width: 14px; height: 14px;
    border-radius: 50%;
    background: var(--gold);
  }
  /* details side */
  .card-details .wordmark {
    position: absolute;
    left: 36px; top: 70px;
    font-size: 34px;
  }
  .divider {
    position: absolute;
    left: 270px; top: 56px;
    width: 1.5px; height: 150px;
    background: var(--gold);
  }
  .tagline {
    position: absolute;
    left: 36px; bottom: 34px;
    color: var(--gold);
    font-size: 14px;
    font-weight: 500;
    letter-spacing: 0.4px;
    text-transform: uppercase;
  }
  .contact {
    position: absolute;
    left: 292px; top: 58px;
    font-size: 13px;
    line-height: 1.45;
  }
  .contact-name {
    color: var(--gold);
    font-weight: 700;
    text-transform: uppercase;
    font-size: 14px;
  }
  .contact-title { font-weight: 500; margin-bottom: 4px; }
  .contact-line { display: flex; align-items: center; gap: 7px; }
  .contact-line svg { width: 12px; height: 12px; flex: none; }
  /* logo side */
  .card-front { display: flex; align-items: center; justify-content: center; }
  .card-front .wordmark { font-size: 58px; gap: 16px; }
  .card-front .wordmark-dot { width: 22px; height: 22px; }
</style>
</head>
<body>
  <section class="card card-details">
    <div class="wordmark"><span class="wordmark-dot"></span>Brimovex</div>
    <div class="divider"></div>
    <div class="contact">
      <p class="contact-name">Dane Calloway</p>
      <p class="contact-title">Managing Director</p>
      <p>48 Harbor Crest Lane,</p>
      <p>Oakridge, ON M2K 1P7</p>
      <p class="contact-line">
        <svg viewBox="0 0 12 12"><path fill="#c8c127" d="M2.4 1h2l1 2.6-1.3.9a6.5 6.5 0 0 0 3.4 3.4l.9-1.3 2.6 1v2c0 .6-.5 1.1-1.1 1.1A9.6 9.6 0 0 1 1.3 2.1C1.3 1.5 1.8 1 2.4 1z"/></svg>
        +5693627140
      </p>
      <p class="contact-line">
        <svg viewBox="0 0 12 12"><rect x="1" y="2.5" width="10" height="7" rx="1" fill="#c8c127"/><path d="M1.5 3l4.5 3.3L10.5 3" stroke="#072a25" stroke-width="1" fill="none"/></svg>
        info@brimovex.com
      </p>
      <p class="contact-line">
        <svg viewBox="0 0 12 12"><circle cx="6" cy="6" r="5" fill="none" stroke="#c8c127" stroke-width="1.2"/><ellipse cx="6" cy="6" rx="2.2" ry="5" fill="none" stroke="#c8c127" stroke-width="1"/><path d="M1 6h10" stroke="#c8c127" stroke-width="1"/></svg>
        www.brimovex.com
      </p>
    </div>
    <p class="tagline">Your furry friends deserves the best</p>
  </section>

  <section class="card card-front">
    <div class="wordmark"><span class="wordmark-dot"></span>Brimovex</div>
  </section>
</body>
</html>
```